simple attractive bottled purified natural water label

Looking for a logo design, for a bottled water house brand.The Name of the water is "Toro-K" Natural Purified water I have attached 2 images, In the Mandel Image, I Like the top Left water design, the bold Red Name really stands out.I like the placement of the Font with the Natural Purified water,On the 2nd image Russian one, I again like the red bold, the bird flying out is interesting, not sure if a concept could rather use a seabird / gul or a albatros type, with the same effectThe blue colours in bother these designs are great.Many tahnks

Target Market(s)

Young crowd

Font styles to use
Sans Serif

Colors
0455a3
3276b5
ffffff
33a6d7
85cae6
85acd3
0692cd
ec1f27

Requirements
Must have
• some red in the label to make it pop.
• simple design
Nice to have
• the idea of a Gull ( Bird ) flying out to signify free pure natural.

```html
<!DOCTYPE html>
<html lang="en">
<head>
<meta charset="utf-8">
<title>Toro-K Natural Spring Water Label</title>
<link href="https://fonts.googleapis.com/css2?family=Poppins:wght@500&family=Roboto:wght@400&display=swap" rel="stylesheet">
<style>
  :root {
    --backdrop: #e2e2e4;
    --label: #ffffff;
    --ink: #1d1d1f;
    --red: #ec1f27;
    --blue-deep: #0455a3;
    --blue-mid: #3276b5;
    --blue-bright: #0692cd;
    --blue-sky: #33a6d7;
    --blue-soft: #85cae6;
    --grey-text: #3a3a3c;
  }
  html, body {
    margin: 0;
    width: 1200px;
    height: 919px;
    overflow: hidden;
    background: var(--backdrop);
  }
  .canvas {
    width: 1200px;
    height: 919px;
    display: flex;
    align-items: center;
    justify-content: center;
  }
  .label {
    width: 620px;
    background: var(--label);
    padding: 40px 0 36px;
    display: flex;
    flex-direction: column;
    align-items: center;
    box-shadow: 0 2px 10px rgba(0, 0, 0, 0.06);
  }
  .brand-name {
    font-family: "Poppins", sans-serif;
    font-weight: 500;
    font-size: 150px;
    line-height: 1;
    letter-spacing: -2px;
    color: var(--ink);
    margin: 0;
  }
  .wave-band {
    width: 620px;
    height: 190px;
    margin-top: 10px;
    background: linear-gradient(
      to bottom,
      var(--blue-deep) 0%,
      var(--blue-mid) 30%,
      var(--blue-bright) 55%,
      var(--blue-sky) 78%,
      var(--blue-soft) 100%
    );
  }
  .variant {
    display: flex;
    align-items: center;
    gap: 18px;
    margin-top: 34px;
    font-family: "Roboto", sans-serif;
    font-size: 22px;
    letter-spacing: 6px;
    color: var(--red);
  }
  .variant .rule {
    width: 140px;
    height: 1px;
    background: var(--red);
  }
  .descriptor {
    font-family: "Roboto", sans-serif;
    font-size: 22px;
    letter-spacing: 6px;
    color: var(--grey-text);
    margin-top: 10px;
  }
  .volume {
    font-family: "Roboto", sans-serif;
    font-size: 40px;
    color: var(--ink);
    margin-top: 16px;
  }
</style>
</head>
<body>
  <main class="canvas">
    <section class="label">
      <h1 class="brand-name">Toro</h1>

      <div class="wave-band" role="img" aria-label="Decorative pattern of stacked wavy lines in shades of blue with a small red accent"></div>

      <div class="variant">
        <span class="rule"></span>
        <span>TORO-K</span>
        <span class="rule"></span>
      </div>
      <div class="descriptor">NATURAL SPRING WATER</div>
      <div class="volume">500 ml</div>
    </section>
  </main>
</body>
</html>
```